Profesional personal website needs design and business card

I need a business card with my professional name as a logo "Marlo Vitality" for my business. I am a Wellness Coach, consultant and trainer. So it should be professional, wellness oriented and modern.

Target Market(s)

Private clients, governments, corporations. Luxury and high market.

Industry/Entity Type

Health And Wellness

Contact Information for Business Card

Marlo Vitality should be the logo

Colors

Designer to choose colors to be used in the design.

Requirements
Must have
• Marlo Vitality
• Name: Tomás Arribal
• Wellness Coach, Consultant & Trainer.
• Website: www.marlovitality.example
• Phone:
• Spain (+34) 612 480 397
• (USA) +1 (555) 318 2046
Nice to have
• The most important is the design of "Marlo Vitality", as this is going to be my personal brand logo. It should be professional, wellness, high end and actual.
Should not have
• no golds, no baroque style..

```html
<!DOCTYPE html>
<html lang="en">
<head>
<meta charset="utf-8">
<title>Marlo Vitality — Business Card</title>
<link rel="stylesheet" href="https://fonts.googleapis.com/css2?family=Exo+2:wght@500&family=Montserrat:wght@300;400&display=swap">
<style>
  :root {
    --paper: #ffffff;
    --accent: #2f6b62;
    --ink-grey: #858585;
    --photo-dark: #3a2a22;
    --photo-warm: #c9a27a;
    --photo-wine: #8e2a30;
    --photo-sage: #7fb89a;
  }
  * { margin: 0; padding: 0; box-sizing: border-box; }
  html, body { width: 1200px; height: 675px; overflow: hidden; background: var(--paper); }
  .card {
    position: relative;
    width: 1200px;
    height: 675px;
    overflow: hidden;
    background: var(--paper);
    font-family: "Montserrat", Arial, sans-serif;
  }
  .hero-photo { position: absolute; left: 0; top: 0; }
  .brand-mark {
    position: absolute;
    left: 888px; top: 114px;
    width: 42px; height: 42px;
    border-radius: 50%;
    background: var(--accent);
  }
  .brand-name {
    position: absolute;
    left: 660px; width: 500px; top: 224px;
    text-align: center;
    font-family: "Exo 2", Arial, sans-serif;
    font-weight: 500;
    font-size: 57px;
    line-height: 1;
    color: var(--accent);
  }
  .brand-tagline {
    position: absolute;
    left: 700px; width: 440px; top: 324px;
    text-align: center;
    font-weight: 300;
    font-size: 30px;
    letter-spacing: 0.4em;
    line-height: 1;
    color: var(--accent);
  }
  .person-name {
    position: absolute;
    left: 0; width: 1220px; top: 464px;
    text-align: center;
    font-weight: 400;
    font-size: 35px;
    letter-spacing: 0.22em;
    line-height: 1;
    color: var(--accent);
  }
  .person-role {
    position: absolute;
    left: 0; width: 1204px; top: 521px;
    text-align: center;
    font-weight: 300;
    font-size: 31px;
    letter-spacing: 0.03em;
    line-height: 1;
    color: var(--ink-grey);
  }
  .website {
    position: absolute;
    left: 2px; top: 654px;
    font-weight: 300;
    font-size: 17px;
    letter-spacing: 0.03em;
    color: var(--ink-grey);
  }
  .phones {
    position: absolute;
    right: 19px; top: 630px;
    text-align: right;
    font-weight: 300;
    font-size: 18px;
    letter-spacing: 0.03em;
    line-height: 23px;
    color: var(--ink-grey);
  }
</style>
</head>
<body>
  <main class="card">
    <svg class="hero-photo" width="832" height="455" viewBox="0 0 832 455" role="img" aria-label="Spa still life photograph: lit candles, rolled towels and wicker balls in warm tones">
      <defs>
        <linearGradient id="spa-tones" x1="0" y1="0" x2="1" y2="0.6">
          <stop offset="0" stop-color="var(--photo-dark)"/>
          <stop offset="0.3" stop-color="var(--photo-warm)"/>
          <stop offset="0.55" stop-color="var(--photo-sage)"/>
          <stop offset="0.8" stop-color="var(--photo-wine)"/>
          <stop offset="1" stop-color="var(--photo-wine)"/>
        </linearGradient>
      </defs>
      <polygon points="8,0 830,0 8,453" fill="url(#spa-tones)"/>
    </svg>

    <div class="brand-mark" aria-hidden="true"></div>
    <h1 class="brand-name">Marlo Vitality</h1>
    <p class="brand-tagline">WELLNESS SPA</p>

    <h2 class="person-name">TOMÁS ARRIBAL</h2>
    <p class="person-role">WELLNESS COACH, CONSULTANT &amp; TRAINER</p>

    <p class="website">WEBSITE: WWW.MARLOVITALITY.EXAMPLE</p>
    <p class="phones">SPAIN (+34) 612 480 397<br>(USA) +1 (555) 318 2046</p>
  </main>
</body>
</html>
```